A website design for a consultation firm

We are located in Istanbul, Turkey and offers our consultation services to customers interested in investing in Realestate, Education and Investment particularly this coming from Arab world and English speaking countries.

The site should carry our message of deep knowledge about the Turkish markets in the mentioned sectors of interest, sincerity and keenness.

The final deliverable of the winning design should include:
- The source files of the final designs. e.g. AI, PSD ..etc
- The redline markup for the design using a Specctr or any other similar tool.

Target Market(s)

English and Arabic speaking countries with a Turkish theme since we are a Turkish company

Industry/Entity Type

Consulting

Number of Pages Required

2 page

Font styles to use
Sans Serif

Requirements
Must have
• The site should serve the following main sections:
• - Why QVD?
• - Reports & studies
• - Sectors
• - Our team
• - Contact
• We need a design that could be converted into a WordPress theme.
• The design should be in English but should accommodate other languages including RTL.
• You can use the color theme you like as long as it does't dissolve the logo.
• The site should link into our accounts on the following networks:
• - Twitter
• - Facebook
• - LinkedIn
• The design should be responsive and nicely rendered on Desktop, Tablets and Smart phones.
Nice to have
• The site would be nice to balance between being informative and

```html
<!DOCTYPE html>
<html lang="en">
<head>
<meta charset="utf-8">
<title>QVD Consulting</title>
<link href="https://fonts.googleapis.com/css2?family=Raleway:wght@500;700;800&family=Open+Sans:wght@400;600;700&display=swap" rel="stylesheet">
<style>
:root{
  --navy:#1c2858;
  --navy-deep:#141d42;
  --red:#c81f2e;
  --ink:#333842;
  --muted:#7a7f8a;
  --line:#e3e5ea;
  --light:#f3f4f6;
  --footer:#2b2d31;
  --footer-deep:#1f2023;
  --white:#ffffff;
}
*{box-sizing:border-box;margin:0;padding:0}
html,body{width:1200px;height:2408px;overflow:hidden}
body{font-family:"Open Sans",Arial,sans-serif;color:var(--ink);background:var(--white);position:relative;font-size:12px}
.heading{font-family:"Raleway",Arial,sans-serif;font-weight:800;color:var(--navy);text-transform:uppercase;letter-spacing:1px}
.wrap{position:absolute;left:132px;width:936px}

/* top bar */
.topbar{position:absolute;top:0;left:0;width:1200px;height:32px;background:var(--navy-deep);color:#c9cde0;font-size:11px}
.topbar .contact{position:absolute;left:132px;top:9px;display:flex;gap:26px}
.topbar .social{position:absolute;right:132px;top:10px;display:flex;gap:12px}
.dot-icon{width:12px;height:12px;border-radius:50%;background:#c9cde0;display:block}

/* header */
.header{position:absolute;top:32px;left:0;width:1200px;height:128px;background:var(--white);border-bottom:1px solid var(--line)}
.brand{position:absolute;left:132px;top:30px;display:flex;align-items:center;gap:12px}
.brand .mark{width:40px;height:40px;border-radius:50%;background:var(--red)}
.brand .name{font-family:"Raleway",sans-serif;font-weight:800;font-size:30px;color:var(--navy);line-height:1}
.brand .name small{display:block;font-size:13px;font-weight:800;letter-spacing:1px;margin-top:4px}
.lang{position:absolute;right:132px;top:40px;font-size:11px;color:var(--navy);font-weight:700}
.nav{position:absolute;right:132px;top:80px;display:flex;gap:40px;font-family:"Raleway",sans-serif;font-weight:700;font-size:11px;color:var(--navy);text-transform:uppercase;letter-spacing:.5px}

/* hero */
.hero{position:absolute;top:160px;left:0;width:1200px;height:432px;background:linear-gradient(180deg,#3b5b8f 0%,#2a4270 45%,#4a4f63 80%,#6a5b4e 100%)}
.hero-text{position:absolute;top:120px;left:0;width:1200px;text-align:center;color:var(--white)}
.hero-text h1{font-family:"Raleway",sans-serif;font-weight:800;font-size:40px;letter-spacing:3px}
.hero-text p{font-size:13px;letter-spacing:1.5px;text-transform:uppercase;margin-top:14px;font-weight:600}
.btn{display:inline-block;background:var(--navy);color:var(--white);font-family:"Raleway",sans-serif;font-weight:700;font-size:11px;letter-spacing:1px;padding:10px 22px;margin-top:28px}
.slider-dots{position:absolute;top:364px;left:0;width:1200px;display:flex;justify-content:center;gap:10px}
.slider-dots span{width:9px;height:9px;border-radius:50%;background:rgba(255,255,255,.5)}
.slider-dots span.active{background:var(--white)}

/* about */
.about{top:620px}
.about .col{position:absolute;top:0;width:440px}
.about .col.right{left:496px}
.section-title{font-size:26px;padding-bottom:10px;border-bottom:2px solid var(--line);position:relative}
.section-title::after{content:"";position:absolute;left:0;bottom:-2px;width:60px;height:2px;background:var(--red)}
.col.right .section-title{font-size:20px}
.about p{font-size:11.5px;line-height:1.7;color:var(--muted);margin-top:18px}
.read-more{display:inline-flex;align-items:center;gap:8px;margin-top:26px;font-size:12px;color:var(--navy);font-weight:600}
.bars{margin-top:26px}
.bar{margin-bottom:24px}
.bar .label{display:flex;justify-content:space-between;font-family:"Raleway",sans-serif;font-weight:700;font-size:10.5px;color:var(--navy);text-transform:uppercase;margin-bottom:6px}
.bar .track{height:7px;background:var(--navy)}
.bar .fill{height:7px;background:var(--red)}

/* services */
.services{position:absolute;top:880px;left:0;width:1200px;height:480px;background:var(--light);border-top:1px solid var(--line)}
.centered-title{text-align:center;font-size:30px;position:absolute;top:66px;left:0;width:1200px}
.centered-title::after{content:"";display:block;width:60px;height:2px;background:var(--red);margin:12px auto 0}
.card{position:absolute;top:152px;width:272px;height:252px;background:var(--white);border:1px solid var(--line);text-align:center}
.card .icon{width:84px;height:84px;border-radius:50%;background:var(--white);border:1px solid var(--line);margin:-24px auto 0;display:flex;align-items:center;justify-content:center}
.card h3{font-family:"Raleway",sans-serif;font-weight:800;font-size:15px;color:var(--navy);margin-top:28px;text-transform:uppercase}
.card p{font-size:11px;line-height:1.7;color:var(--muted);margin:14px 26px 0}
.card a{display:block;font-size:11px;color:var(--navy);font-weight:600;margin-top:16px}

/* testimonials */
.testimonials{position:absolute;top:1360px;left:0;width:1200px;height:312px;background:linear-gradient(180deg,#1e2f66 0%,#243a78 50%,#1a2a5e 100%)}
.testimonials h2{color:var(--white);text-align:center;font-family:"Raleway",sans-serif;font-weight:800;font-size:30px;letter-spacing:1px;margin-top:70px}
.testimonials h2::after{content:"";display:block;width:60px;height:2px;background:var(--red);margin:12px auto 0}
.testimonials p{color:#dfe3f0;text-align:center;font-size:12px;line-height:1.7;width:936px;margin:24px auto 0}
.testimonials .author{display:block;margin-top:14px;font-weight:700;color:var(--white)}

/* team */
.team{top:1728px}
.team .title{font-size:30px}
.arrows{position:absolute;right:0;top:6px;display:flex;gap:6px}
.arrows span{width:26px;height:26px;border:1px solid #c8ccd5;display:flex;align-items:center;justify-content:center}
.member{position:absolute;top:76px;width:212px;height:240px;background:linear-gradient(180deg,#8a9aa8 0%,#5e6b78 100%);overflow:hidden}
.member .plate{position:absolute;left:0;bottom:0;width:100%;padding:10px;background:rgba(28,40,88,.9);text-align:center;color:var(--white)}
.member .plate b{font-family:"Raleway",sans-serif;font-weight:800;font-size:13px;letter-spacing:1px;display:block}
.member .plate small{font-size:10px;color:#c9cde0}
.member.featured .plate{top:0;bottom:auto;height:100%;padding-top:30px}
.member.featured .plate p{font-size:10px;line-height:1.6;color:#c9cde0;margin:12px 14px 0}
.member.featured .icons{display:flex;justify-content:center;gap:10px;margin-top:16px}

/* footer */
.footer{position:absolute;top:2088px;left:0;width:1200px;height:264px;background:var(--footer);color:#a9adb5}
.footer .fcol{position:absolute;top:36px}
.footer h4{font-family:"Raleway",sans-serif;font-weight:700;font-size:12px;color:var(--white);text-transform:uppercase;letter-spacing:1px;padding-bottom:8px;border-bottom:1px solid #45484f;margin-bottom:14px}
.footer ul{list-style:none;font-size:11px;line-height:1.9}
.footer p{font-size:11px;line-height:1.7}
.footer-brand{display:flex;align-items:center;gap:10px;margin-top:14px}
.footer-brand .mark{width:36px;height:36px;border-radius:50%;background:#8b8f97}
.footer-brand span{font-family:"Raleway",sans-serif;font-weight:800;font-size:26px;color:#8b8f97}
.footer .social{display:flex;gap:10px;margin-top:24px}
.input{margin-top:14px;height:30px;width:190px;background:#3a3d43;font-size:10px;color:#8b8f97;padding:8px 10px}
.subscribe{margin-top:12px;display:inline-block;background:var(--navy);color:var(--white);font-size:10px;font-weight:700;padding:8px 14px;letter-spacing:1px}
.contact-row{display:flex;align-items:center;gap:10px;font-size:11px;margin-bottom:12px}
.bottombar{position:absolute;top:2352px;left:0;width:1200px;height:56px;background:var(--footer-deep);color:#8b8f97;font-size:10.5px;text-align:center;padding-top:20px}
</style>
</head>
<body>

<div class="topbar">
  <div class="contact">
    <span>&#9742; +90 212 555 0147</span>
    <span>&#9993; info@qvdconsult.com</span>
  </div>
  <div class="social">
    <span class="dot-icon"></span><span class="dot-icon"></span><span class="dot-icon"></span>
  </div>
</div>

<header class="header">
  <div class="brand">
    <span class="mark"></span>
    <div class="name">QVD<small>consulting</small></div>
  </div>
  <div class="lang">EN &#9662;</div>
  <nav class="nav">
    <span>Home</span><span>Why QVD</span><span>Reports &amp; Studies</span><span>Sectors</span><span>Our Team</span><span>Contact</span>
  </nav>
</header>

<section class="hero" role="img" aria-label="Istanbul mosque skyline at dusk under a blue sky">
  <div class="hero-text">
    <h1>CONSULTATION SERVICES</h1>
    <p>Customers interested in investing in real estate, education and investment</p>
    <span class="btn">LEARN MORE</span>
  </div>
  <div class="slider-dots"><span></span><span class="active"></span><span></span></div>
</section>

<section class="wrap about">
  <div class="col">
    <h2 class="heading section-title">About Us</h2>
    <p>Our team brings deep knowledge of the Turkish market to every client. We guide investors from the Arab world and English speaking countries through real estate, education and financial choices with sincerity and keen attention to detail, from first contact to final signature.</p>
    <span class="read-more">Read more
      <svg width="16" height="10" viewBox="0 0 16 10"><path d="M0 5h14M10 1l4 4-4 4" stroke="#1c2858" stroke-width="1.5" fill="none"/></svg>
    </span>
  </div>
  <div class="col right">
    <h2 class="heading section-title">Reports &amp; Studies</h2>
    <div class="bars">
      <div class="bar"><div class="label"><span>Real Estate</span><span>80%</span></div><div class="track"><div class="fill" style="width:80%"></div></div></div>
      <div class="bar"><div class="label"><span>Education</span><span>60%</span></div><div class="track"><div class="fill" style="width:60%"></div></div></div>
      <div class="bar"><div class="label"><span>Finance Support</span><span>90%</span></div><div class="track"><div class="fill" style="width:90%"></div></div></div>
    </div>
  </div>
</section>

<section class="services">
  <h2 class="heading centered-title">Our Services</h2>
  <div class="card" style="left:144px">
    <div class="icon"><svg width="30" height="28" viewBox="0 0 30 28"><path d="M15 2L2 14h4v12h7v-8h4v8h7V14h4z" fill="#1c2858"/></svg></div>
    <h3>Real Estate</h3>
    <p>Trusted guidance on homes, land and commercial property across Istanbul and the wider Turkish market.</p>
    <a>Read more &rarr;</a>
  </div>
  <div class="card" style="left:464px">
    <div class="icon"><svg width="28" height="30" viewBox="0 0 28 30"><path d="M4 3h18a2 2 0 0 1 2 2v22H7a3 3 0 0 1-3-3z" fill="#1c2858"/><path d="M7 24h17" stroke="#fff" stroke-width="1.5"/></svg></div>
    <h3>Education</h3>
    <p>Support choosing Turkish schools and universities, from admission files to student residence permits.</p>
    <a>Read more &rarr;</a>
  </div>
  <div class="card" style="left:784px">
    <div class="icon"><svg width="32" height="28" viewBox="0 0 32 28"><rect x="2" y="7" width="28" height="19" rx="2" fill="#1c2858"/><path d="M11 7V4h10v3" stroke="#1c2858" stroke-width="2.5" fill="none"/><path d="M2 15h28" stroke="#fff" stroke-width="1.5"/></svg></div>
    <h3>Financial</h3>
    <p>Clear advice on investment options, banking, company setup and the legal steps of doing business.</p>
    <a>Read more &rarr;</a>
  </div>
</section>

<section class="testimonials" role="img" aria-label="Desk with documents and a laptop in blue tones">
  <h2>TESTIMONIALS</h2>
  <p>The team explained every step of buying our apartment in Istanbul with patience and honesty. Their market knowledge saved us time and money, and they stayed with us long after the keys were handed over.
    <span class="author">Ahmed Karim</span></p>
</section>

<section class="wrap team">
  <h2 class="heading title">Our Team</h2>
  <div class="arrows">
    <span><svg width="8" height="10" viewBox="0 0 8 10"><path d="M6 1L2 5l4 4" stroke="#1c2858" stroke-width="1.5" fill="none"/></svg></span>
    <span><svg width="8" height="10" viewBox="0 0 8 10"><path d="M2 1l4 4-4 4" stroke="#1c2858" stroke-width="1.5" fill="none"/></svg></span>
  </div>
  <div class="member featured" style="left:0" role="img" aria-label="Portrait of team member">
    <div class="plate"><b>JOHN DOE</b><small>Managing Partner</small>
      <p>Fifteen years advising overseas investors on Turkish property and finance.</p>
      <div class="icons"><span class="dot-icon"></span><span class="dot-icon"></span><span class="dot-icon"></span></div>
    </div>
  </div>
  <div class="member" style="left:244px" role="img" aria-label="Portrait of team member">
    <div class="plate"><b>JOHN DOE</b><small>Real Estate Advisor</small></div>
  </div>
  <div class="member" style="left:484px" role="img" aria-label="Portrait of team member">
    <div class="plate"><b>JOHN DOE</b><small>Education Advisor</small></div>
  </div>
  <div class="member" style="left:724px" role="img" aria-label="Portrait of team member">
    <div class="plate"><b>JOHN DOE</b><small>Finance Advisor</small></div>
  </div>
</section>

<footer class="footer">
  <div class="fcol" style="left:132px">
    <div class="footer-brand"><span class="mark"></span><span>QVD</span></div>
    <div class="social"><span class="dot-icon"></span><span class="dot-icon"></span><span class="dot-icon"></span></div>
  </div>
  <div class="fcol" style="left:384px;width:180px">
    <h4>Quick Links</h4>
    <ul><li>Home</li><li>Why QVD</li><li>Reports &amp; Studies</li><li>Sectors</li><li>Our Team</li><li>Contact</li></ul>
  </div>
  <div class="fcol" style="left:596px;width:220px">
    <h4>Newsletter</h4>
    <p>Join the newsletter to receive the latest market updates.</p>
    <div class="input">Enter Your Email</div>
    <span class="subscribe">SUBSCRIBE</span>
  </div>
  <div class="fcol" style="left:876px;width:192px">
    <h4>Contact Us</h4>
    <div class="contact-row">&#9742; +90 212 555 0147</div>
    <div class="contact-row">&#9743; +90 212 555 0148</div>
    <div class="contact-row">&#9993; info@qvdconsult.com</div>
    <div class="contact-row">
      <svg width="10" height="14" viewBox="0 0 10 14"><path d="M5 0a5 5 0 0 1 5 5c0 4-5 9-5 9S0 9 0 5a5 5 0 0 1 5-5z" fill="#a9adb5"/><circle cx="5" cy="5" r="2" fill="#2b2d31"/></svg>
      Meridyen Sok. 14, Sisli, Istanbul</div>
  </div>
</footer>
<div class="bottombar">&copy;2024 QVD Consulting. All Rights Reserved.</div>

</body>
</html>
```